Talvena Brooke R&B Mixtape CD Cover

We need a cd cover for an r&b mixtape. The artist's name is Talvena Brooke and the name of the mixtape is 4:17. The cover should reflect a vibe of 4:17 am in the morning where a young female has concluded clubbing and the night is left open ended, meaning it could be the beginning of a whole new morning or the night not ending. The cover should be creative and reflect the essence of a breakout artist. The cover will be used as the visual for all online music posts i.e. mixvault, tunelodge, echoharbor, etc. Artist name and the title of the mixtape should be included on the cover.

Target Market(s)

R&B music lovers aged 19-39.

Industry/Entity Type

Music Download

Requirements
Must have
• Reflecting of time and having a good time.

```html
<!DOCTYPE html>
<html lang="en">
<head>
<meta charset="utf-8">
<title>Talvena Brooke – 4:17 R&amp;B Collection</title>
<link href="https://fonts.googleapis.com/css2?family=Comfortaa:wght@500;700&family=Orbitron:wght@500&display=swap" rel="stylesheet">
<style>
  :root {
    --page-bg: #2a2a2a;
    --cover-black: #050308;
    --violet: #5a1a8c;
    --magenta: #8a1f6a;
    --orange: #e8641c;
    --amber: #f2a526;
    --green: #3fae4a;
    --blue: #1f56c8;
    --sky: #5fa8e8;
    --text-white: #f4f4f6;
    --digit-fill: #e9ecef;
    --digit-edge: #9aa2ab;
  }
  * { margin: 0; padding: 0; box-sizing: border-box; }
  html, body {
    width: 1200px;
    height: 1164px;
    overflow: hidden;
    background: var(--page-bg);
  }
  .cover {
    position: absolute;
    left: 50px;
    top: 32px;
    width: 1100px;
    height: 1100px;
    background: var(--cover-black);
    overflow: hidden;
  }
  .cover-art {
    position: absolute;
    inset: 0;
    background:
      radial-gradient(ellipse 28% 30% at 45% 46%, rgba(242,165,38,0.85), transparent 70%),
      radial-gradient(ellipse 30% 34% at 38% 36%, rgba(232,100,28,0.8), transparent 72%),
      radial-gradient(ellipse 26% 30% at 62% 50%, rgba(63,174,74,0.35), transparent 70%),
      radial-gradient(ellipse 32% 36% at 76% 48%, rgba(31,86,200,0.85), transparent 72%),
      radial-gradient(ellipse 26% 22% at 72% 22%, rgba(95,168,232,0.45), transparent 72%),
      radial-gradient(ellipse 40% 40% at 20% 24%, rgba(138,31,106,0.75), transparent 75%),
      radial-gradient(ellipse 40% 45% at 6% 14%, rgba(90,26,140,0.9), transparent 75%),
      radial-gradient(ellipse 45% 30% at 55% 86%, rgba(20,24,40,0.9), transparent 80%),
      var(--cover-black);
  }
  .artist-name {
    position: absolute;
    left: 42px;
    top: 52px;
    font-family: "Comfortaa", sans-serif;
    font-weight: 700;
    font-size: 80px;
    letter-spacing: 1px;
    color: var(--text-white);
    text-shadow: 0 2px 6px rgba(0,0,0,0.6);
  }
  .mixtape-title {
    position: absolute;
    left: 130px;
    top: 340px;
    width: 840px;
    height: 360px;
  }
  .mixtape-title text {
    font-family: "Orbitron", sans-serif;
    font-weight: 500;
    font-size: 330px;
    fill: var(--digit-fill);
    fill-opacity: 0.82;
    stroke: var(--digit-edge);
    stroke-width: 4;
  }
  .collection-tag {
    position: absolute;
    right: 28px;
    bottom: 60px;
    text-align: center;
    font-family: "Comfortaa", sans-serif;
    font-weight: 700;
    color: var(--text-white);
    text-shadow: 0 2px 6px rgba(0,0,0,0.6);
  }
  .collection-tag .genre {
    display: block;
    font-size: 104px;
    line-height: 0.95;
  }
  .collection-tag .label {
    display: block;
    font-size: 44px;
    line-height: 1;
  }
</style>
</head>
<body>
  <main class="cover">
    <div class="cover-art" role="img" aria-label="Night-club artwork: guitar neck and aviator sunglasses in a rainbow glow of violet, orange and blue with soft swirls"></div>
    <h1 class="artist-name">Talvena Brooke</h1>
    <svg class="mixtape-title" viewBox="0 0 840 360" aria-label="4:17">
      <defs>
        <filter id="digit-shadow" x="-10%" y="-10%" width="120%" height="130%">
          <feDropShadow dx="0" dy="6" stdDeviation="6" flood-color="#000" flood-opacity="0.55"/>
        </filter>
      </defs>
      <text x="420" y="300" text-anchor="middle" filter="url(#digit-shadow)">4:17</text>
    </svg>
    <div class="collection-tag">
      <span class="genre">R&amp;B</span>
      <span class="label">collection</span>
    </div>
  </main>
</body>
</html>
```